Redesign website bus travel company Lenz Tavan

We require a complete redesign of the website of Reisebüro Lenz Tavan, an established bus tour operator based in Graubünden (www.lenztavan-beispiel.ch). For years, the company has specialized in multi-day tours throughout Europe, as well as day trips such as shopping trips to Innsbruck or Como, music tours, and market visits, primarily for seniors, as well as car rentals for clubs and companies.

The new website requires a video header with overlay text, red as the primary corporate color, complemented by black and gray, and a highly simplified navigation with two main sections: "Our Trips" and "Bus Rental." The remaining sections must be accessible via the "Menu" menu item. The design should be user-friendly for all age groups and mobile-responsive.

The goal is a trustworthy, modern website that reflects personal service and many years of experience.
The new logo can be found in the files, as well as a few pictures.

Target Market(s)

Guests of bus tours (day and multi-day trips) and bus rentals (clubs, companies, etc.)

Industry/Entity Type

Busreisen und Busvermietung

Number of Pages Required

1 page

Requirements
Must have
• Red as primary color, video header, simple UX for target group seniors
Nice to have
• Photo galleries of destinations and the vehicle fleet

```html
<!DOCTYPE html>
<html lang="en">
<head>
<meta charset="utf-8">
<title>Lenz Tavan – Bus Travel</title>
<link rel="stylesheet" href="https://fonts.googleapis.com/css2?family=Marcellus&family=Poppins:wght@400;500;700&family=Work+Sans:wght@400&display=swap">
<style>
  :root {
    --red: #a8141c;
    --red-dark: #8a1016;
    --black: #1b1b1b;
    --gray: #5c5c5c;
    --gray-light: #ecebea;
    --paper: #fbfaf9;
    --white: #ffffff;
  }
  * { box-sizing: border-box; margin: 0; padding: 0; }
  html, body { width: 1200px; height: 4011px; overflow: hidden; }
  body {
    position: relative;
    background: var(--paper);
    color: var(--black);
    font-family: "Poppins", sans-serif;
    border-top: 3px solid var(--black);
  }
  a { color: inherit; text-decoration: none; }
  .abs { position: absolute; }
  .serif { font-family: "Marcellus", serif; text-transform: uppercase; font-weight: 400; }

  /* header */
  .brand-mark { left: 28px; top: 34px; font-family: "Marcellus", serif; font-size: 17px; letter-spacing: .5px; text-transform: uppercase; color: var(--red); }
  .nav-link { top: 37px; font-size: 12px; color: var(--black); padding-bottom: 4px; text-transform: uppercase; }
  .nav-link.is-active { border-bottom: 1px solid var(--red); color: var(--red); }
  .nav-menu { left: 1010px; top: 20px; width: 162px; height: 48px; background: var(--red); color: var(--white); font-size: 12px; font-weight: 500; display: flex; align-items: center; justify-content: center; gap: 10px; text-transform: uppercase; }

  /* hero */
  .hero-title { left: 100px; width: 1000px; top: 202px; text-align: center; font-size: 44px; line-height: 48px; color: var(--red); }
  .hero-tag { left: 0; width: 1200px; top: 368px; text-align: center; font-family: "Work Sans", sans-serif; font-size: 15px; color: var(--gray); }
  .btn-solid { background: var(--red); color: var(--white); font-size: 12px; font-weight: 500; display: flex; align-items: center; justify-content: center; }
  .hero-cta { left: 490px; top: 410px; width: 221px; height: 46px; }
  .hero-video { left: 53px; top: 517px; width: 1095px; height: 675px; border-radius: 16px; overflow: hidden;
    background: linear-gradient(180deg, #5a6f86 0%, #3a3a40 40%, #2a2422 75%, #3b3a3c 100%); }
  .hero-video-shade { position: absolute; inset: 0; background: linear-gradient(180deg, rgba(0,0,0,0) 45%, rgba(0,0,0,.6) 100%); }
  .hero-overlay { position: absolute; left: 48px; bottom: 44px; color: var(--white); }
  .hero-overlay-kicker { font-family: "Work Sans", sans-serif; font-size: 15px; margin-bottom: 6px; }
  .hero-overlay-title { font-family: "Marcellus", serif; text-transform: uppercase; font-size: 30px; line-height: 34px; }
  .hero-play { position: absolute; right: 48px; bottom: 44px; width: 64px; height: 64px; border-radius: 50%; border: 2px solid var(--white); display: flex; align-items: center; justify-content: center; }

  /* trips */
  .trips { left: 0; top: 1240px; width: 1200px; height: 791px; background: var(--red); }
  .trips-kicker { left: 0; width: 1200px; top: 1352px; text-align: center; font-family: "Work Sans", sans-serif; font-size: 14px; color: var(--white); }
  .trips-title { left: 0; width: 1200px; top: 1378px; text-align: center; font-size: 31px; color: var(--white); }
  .trip { position: absolute; width: 350px; color: var(--white); }
  .trip h3 { font-family: "Marcellus", serif; font-weight: 400; text-transform: uppercase; font-size: 23px; margin-bottom: 8px; }
  .trip p { font-size: 15.5px; line-height: 23px; margin-bottom: 14px; }
  .btn-outline { width: 240px; height: 46px; border: 1px solid var(--white); font-size: 12px; display: flex; align-items: center; justify-content: center; }

  /* rental */
  .rental-line { left: 0; top: 2656px; width: 604px; height: 1px; background: #cfcfcf; }
  .rental-kicker { left: 42px; top: 2104px; font-family: "Work Sans", sans-serif; font-size: 14px; color: var(--gray); }
  .rental-title { left: 42px; top: 2130px; width: 300px; font-size: 29px; line-height: 32px; color: var(--red); }
  .rental-sub { left: 42px; top: 2384px; font-size: 17px; color: var(--red); }
  .rental-copy { left: 42px; top: 2418px; width: 510px; font-family: "Work Sans", sans-serif; font-size: 14.5px; line-height: 18px; }
  .rental-cta { left: 42px; top: 2540px; width: 240px; height: 46px; }
  .rental-media { left: 604px; top: 2031px; width: 596px; height: 625px;
    background: linear-gradient(180deg, #0f6d89 0%, #1a6f88 45%, #6d7478 70%, #8a8d90 100%); }

  /* gallery */
  .tile { top: 2697px; width: 196px; height: 196px; }
  .t1 { left: 81px; background: linear-gradient(160deg, #b7bcc0, #5a5f60); }
  .t2 { left: 293px; background: linear-gradient(180deg, #9aa9a8, #5e8a3a 55%, #3f6b25); }
  .t3 { left: 506px; background: linear-gradient(180deg, #6f7f80, #505c4f 50%, #9b958c); }
  .t4 { left: 719px; background: linear-gradient(135deg, #2a1b22, #d98a5a 55%, #5a4a60); }
  .t5 { left: 931px; background: linear-gradient(180deg, #c6b49b, #f2a23b 50%, #6a5230); }

  /* contact */
  .contact-media { left: 0; top: 2940px; width: 1200px; height: 646px;
    background: linear-gradient(110deg, #3b4446 0%, #6e3a34 25%, #5d5d5a 55%, #a79c8e 100%); }
  .contact-card { left: 691px; top: 2982px; width: 450px; height: 560px; background: var(--paper); }
  .contact-title { left: 738px; top: 3026px; font-size: 38px; color: var(--red); }
  .contact-lead { left: 738px; top: 3080px; width: 360px; font-size: 16.5px; line-height: 26px; }
  .field { position: absolute; left: 738px; width: 355px; border-bottom: 1px solid var(--gray); font-size: 13px; color: var(--gray); }
  .contact-send { left: 855px; top: 3444px; width: 240px; height: 46px; }

  /* footer */
  .footer { left: 0; top: 3586px; width: 1200px; height: 425px; background: var(--black); color: var(--white); }
  .footer .abs { color: var(--white); }
  .f-brand { left: 29px; top: 60px; font-weight: 700; font-size: 26px; }
  .f-nav { top: 62px; font-size: 14px; padding-bottom: 4px; }
  .f-nav.is-active { border-bottom: 1px solid var(--white); }
  .f-text { left: 29px; top: 170px; font-size: 21px; line-height: 25px; }
  .f-more { left: 115px; top: 240px; font-size: 12px; text-decoration: underline; }
  .f-label { top: 178px; font-family: "Marcellus", serif; text-transform: uppercase; font-size: 17px; }
  .f-info { top: 216px; font-size: 15px; line-height: 24px; font-weight: 500; }
  .f-rule { left: 29px; top: 355px; width: 1144px; height: 1px; background: var(--red); }
  .f-copy { left: 29px; top: 389px; font-size: 11px; }
  .f-social { top: 384px; font-size: 12px; font-weight: 500; display: flex; align-items: center; gap: 5px; }
  .f-social i { width: 8px; height: 8px; background: var(--red); display: inline-block; }
</style>
</head>
<body>
  <header>
    <div class="abs brand-mark">Lenz Tavan</div>
    <nav>
      <a class="abs nav-link is-active" style="left:800px;">Our Trips</a>
      <a class="abs nav-link" style="left:895px;">Bus Rental</a>
      <a class="abs nav-menu">
        <svg width="16" height="12" viewBox="0 0 16 12" aria-hidden="true"><path d="M0 1h16M0 6h16M0 11h16" stroke="#fff" stroke-width="1.6"/></svg>
        Menu
      </a>
    </nav>
  </header>

  <section class="hero">
    <h1 class="abs serif hero-title">Lenz Tavan: Your Go-To Bus Travel Company for Unforgettable European Adventures</h1>
    <p class="abs hero-tag">Travel Beyond the Ordinary!</p>
    <a class="abs btn-solid hero-cta">Book Your Trip Now</a>
    <div class="abs hero-video" role="img" aria-label="Header video: city bus in front of an ornate historic town hall between tall buildings">
      <div class="hero-video-shade"></div>
      <div class="hero-overlay">
        <p class="hero-overlay-kicker">Personal service from Graubünden</p>
        <p class="hero-overlay-title">Day trips and tours across Europe</p>
      </div>
      <div class="hero-play" aria-hidden="true">
        <svg width="22" height="24" viewBox="0 0 22 24"><path d="M4 2l16 10L4 22z" fill="#fff"/></svg>
      </div>
    </div>
  </section>

  <section class="abs trips"></section>
  <p class="abs trips-kicker">Travel with Comfort and Joy</p>
  <h2 class="abs serif trips-title">Explore Our Unique Trips</h2>

  <article class="trip" style="left:51px; top:1484px;">
    <h3>Day Adventures</h3>
    <p>Join us for delightful day trips that whisk you away to charming destinations, perfect for a quick cultural fix or a shopping spree.</p>
    <a class="btn-outline">View Day Adventures</a>
  </article>
  <article class="trip" style="left:426px; top:1484px;">
    <h3>Extended Journeys</h3>
    <p>Experience our thoughtfully crafted multi-day tours, designed to provide comfort and unforgettable memories as you explore Europe.</p>
    <a class="btn-outline">Discover Extended Journeys</a>
  </article>
  <article class="trip" style="left:800px; top:1484px;">
    <h3>Cultural Escapes</h3>
    <p>Engage with local cultures through our specially curated trips, offering immersive experiences that connect you with the heart of each destination.</p>
    <a class="btn-outline">See Cultural Escapes</a>
  </article>
  <article class="trip" style="left:51px; top:1723px;">
    <h3>Market Visits</h3>
    <p>Spend a day wandering through lively markets, where unique finds and leisurely exploration await you at every turn.</p>
    <a class="btn-outline">Shop the Markets</a>
  </article>
  <article class="trip" style="left:426px; top:1723px;">
    <h3>Musical Journeys</h3>
    <p>Join us for enchanting music tours that highlight Europe's vibrant musical heritage, featuring live performances and local talent.</p>
    <a class="btn-outline">Join Musical Journeys</a>
  </article>
  <article class="trip" style="left:800px; top:1723px;">
    <h3>Nature Retreats</h3>
    <p>Reconnect with the great outdoors on nature retreats, where stunning landscapes and peaceful surroundings invite rest and adventure.</p>
    <a class="btn-outline">Explore Nature Retreats</a>
  </article>

  <section class="rental">
    <p class="abs rental-kicker">Ride in Style, Wherever You Go!</p>
    <h2 class="abs serif rental-title">Flexible Bus Rentals for Clubs and Companies</h2>
    <h3 class="abs serif rental-sub">Your Journey, Your Way</h3>
    <p class="abs rental-copy">At Lenz Tavan, we understand that every group has unique needs. Our bus rental options offer the flexibility to tailor your travel experience, whether it's for a corporate event, a club outing, or a special occasion. With our personalized service, we ensure that your journey is as enjoyable as the destination. Sit back, relax, and let us handle the logistics while you focus on making memories!</p>
    <a class="abs btn-solid rental-cta">Request a Quote Today!</a>
    <div class="abs rental-media" role="img" aria-label="Red double-decker bus on a road with historic parliament towers under a blue sky"></div>
    <div class="abs rental-line"></div>
  </section>

  <section class="gallery">
    <div class="abs tile t1" role="img" aria-label="Hand holding a small globe against rocky coastal cliffs"></div>
    <div class="abs tile t2" role="img" aria-label="Hiker on green hills below a rocky pinnacle"></div>
    <div class="abs tile t3" role="img" aria-label="Hiker on a rocky mountain trail"></div>
    <div class="abs tile t4" role="img" aria-label="Sunset seen through an airplane window"></div>
    <div class="abs tile t5" role="img" aria-label="Tent and traveller on a meadow at sunrise"></div>
  </section>

  <section class="contact">
    <div class="abs contact-media" role="img" aria-label="Red double-decker buses on a city street with a traveller waiting at the kerb"></div>
    <div class="abs contact-card"></div>
    <h2 class="abs serif contact-title">Contact Us</h2>
    <p class="abs contact-lead">Got questions or ready to book your next trip? Our dedicated team is just a form away or a quick call!</p>
    <label class="field" style="top:3188px; height:48px;">Name</label>
    <label class="field" style="top:3258px; height:47px;">Email</label>
    <label class="field" style="top:3327px; height:64px;">Message</label>
    <a class="abs btn-solid contact-send">Send Message</a>
  </section>

  <footer class="abs footer">
    <div class="abs f-brand">Lenz Tavan</div>
    <a class="abs f-nav is-active" style="left:615px;">Our Trips</a>
    <a class="abs f-nav" style="left:709px;">Bus Rental</a>
    <p class="abs serif f-text">This is the text area<br>for this paragraph.</p>
    <a class="abs f-more">Learn more</a>
    <div class="abs f-label" style="left:615px;">Contact</div>
    <div class="abs f-info" style="left:615px;">hallo@lenztavan-beispiel.ch<br>+41 81 000 00 00</div>
    <div class="abs f-label" style="left:909px;">Address</div>
    <div class="abs f-info" style="left:909px;">Talstrasse 12, Chur,<br>Schweiz</div>
    <div class="abs f-rule"></div>
    <div class="abs f-copy">© 2025 All Rights Reserved | Company Name</div>
    <div class="abs f-social" style="left:1010px;"><i></i>Feed</div>
    <div class="abs f-social" style="left:1063px;"><i></i>Fotos</div>
    <div class="abs f-social" style="left:1122px;"><i></i>Netz</div>
  </footer>
</body>
</html>
```